Elegant Candy Buffet & Jar Hire Needs a logo & business card design

I need a logo design and a business card design for a new candy buffet company based in Melbourne called "Maple Candy Buffet & Jar Hire"(but the & Jar Hire part to be in smaller font). We set up candy bars with a wide variety of custom themes or to the customer's preference, we also hire out the glass jars if the customer prefers to do it themselves. But i want the emphasis on the front of the business card to be about the Candy Buffet and the jar hire can be at the back of the card. I would like to see designs that use the tiffany blue, or black and gold. I would like to see elegance, class but quite simple.

Industry/Entity Type

Business

Font styles to use
Script

```html
<!DOCTYPE html>
<html lang="en">
<head>
<meta charset="utf-8">
<title>Maple Candy Buffet &amp; Jar Hire – Business Card</title>
<link rel="stylesheet" href="https://fonts.googleapis.com/css2?family=Pinyon+Script&family=Old+Standard+TT&display=swap">
<style>
  :root {
    --tiffany: #7fcfcc;
    --tiffany-soft: #a6dedb;
    --paper: #ffffff;
    --ink-grey: #8c8c8c;
    --jar-grey: #d6d6d6;
    --backdrop: #e8ebeb;
    --card-shadow: rgba(0, 0, 0, 0.18);
  }
  * { box-sizing: border-box; margin: 0; padding: 0; }
  html, body {
    width: 1200px;
    height: 1000px;
    overflow: hidden;
    background: var(--backdrop);
  }
  .canvas {
    position: relative;
    width: 1200px;
    height: 1000px;
  }
  .card {
    position: absolute;
    width: 700px;
    height: 400px;
    background: var(--paper);
    box-shadow: 0 10px 28px var(--card-shadow);
    overflow: hidden;
  }
  .card--front { left: 80px; top: 80px; }
  .card--back { left: 420px; top: 520px; }

  /* Front */
  .damask-fill {
    position: absolute;
    inset: 0;
    background: linear-gradient(135deg, var(--tiffany) 0%, var(--tiffany-soft) 50%, var(--tiffany) 100%);
  }
  .name-plaque {
    position: absolute;
    left: 50%;
    top: 50%;
    width: 280px;
    height: 160px;
    transform: translate(-50%, -50%);
    background: var(--paper);
    display: flex;
    flex-direction: column;
    align-items: center;
    justify-content: center;
    text-align: center;
  }
  .brand-name {
    font-family: "Pinyon Script", cursive;
    color: var(--ink-grey);
    font-weight: 400;
    line-height: 1;
  }
  .brand-name__main { font-size: 64px; display: block; }
  .brand-name__sub { font-size: 26px; display: block; margin-top: 6px; }

  /* Back */
  .damask-band {
    position: absolute;
    left: 0;
    right: 0;
    background: linear-gradient(90deg, var(--tiffany) 0%, var(--tiffany-soft) 50%, var(--tiffany) 100%);
  }
  .damask-band--top { top: 0; height: 95px; }
  .damask-band--bottom { bottom: 0; height: 115px; }
  .jar-illustration {
    position: absolute;
    left: 120px;
    top: 175px;
    width: 150px;
    height: 200px;
    border-radius: 50% 50% 30% 30% / 40% 40% 25% 25%;
    background: radial-gradient(circle at 50% 60%, #eeeeee 0%, var(--jar-grey) 80%);
  }
  .invitation {
    position: absolute;
    left: 310px;
    top: 105px;
    width: 370px;
    text-align: center;
    color: var(--ink-grey);
  }
  .invitation__line {
    font-family: "Pinyon Script", cursive;
    font-size: 30px;
    line-height: 1.15;
  }
  .dot-rule {
    display: block;
    margin: 14px auto 12px;
  }
  .invitation__contact {
    font-family: "Pinyon Script", cursive;
    font-size: 32px;
    line-height: 1.1;
  }
  .invitation__phone {
    font-family: "Old Standard TT", serif;
    font-size: 19px;
    letter-spacing: 2px;
    margin-top: 2px;
  }
</style>
</head>
<body>
<main class="canvas">

  <section class="card card--front">
    <div class="damask-fill" role="img" aria-label="Tiffany blue damask pattern covering the card"></div>
    <div class="name-plaque">
      <h1 class="brand-name">
        <span class="brand-name__main">Maple</span>
        <span class="brand-name__sub">Candy Buffet &amp; Jar Hire</span>
      </h1>
    </div>
  </section>

  <section class="card card--back">
    <div class="damask-band damask-band--top" role="img" aria-label="Tiffany blue damask pattern band"></div>
    <div class="damask-band damask-band--bottom" role="img" aria-label="Tiffany blue damask pattern band"></div>
    <div class="jar-illustration" role="img" aria-label="Pencil sketch of a lidded glass candy jar filled with sweets"></div>
    <div class="invitation">
      <p class="invitation__line">Enjoy some sweet decadence at<br>your next special event.</p>
      <svg class="dot-rule" width="160" height="6" viewBox="0 0 160 6" aria-hidden="true">
        <line x1="3" y1="3" x2="157" y2="3" stroke="var(--tiffany)" stroke-width="4" stroke-linecap="round" stroke-dasharray="0 9"/>
      </svg>
      <p class="invitation__contact">Please contact Clara</p>
      <p class="invitation__phone">0400 555 019</p>
    </div>
  </section>

</main>
</body>
</html>
```